Lumo Brew Premium Matcha brand Label

This is a label design project for a luxury tea brand. Feel free to be creative within the guidelines.
Attached to this project is a document called “Private Label Design Requirements” with the design guidelines and template. There is another document called "Lumo Brew Packaging Instructions" this has more details necessary to stick to the guidelines in the first document.

I have also attached the certifications to be included as well as different variations of the logo for you to use.

If you have any questions, I am here.
Updates

Target Market(s)

Young, active, fun, enjoy the finer things

```html
<!DOCTYPE html>
<html lang="en">
<head>
<meta charset="utf-8">
<title>Lumo Brew – Premium Organic Ceremonial Matcha Label</title>
<link rel="stylesheet" href="https://fonts.googleapis.com/css2?family=Comfortaa:wght@400;500;600;700&display=swap">
<style>
  :root {
    --bg: #e6e6e6;
    --black: #030303;
    --kraft: #e4ddd0;
    --gold: #c99a45;
    --gold-light: #f2d48a;
    --gold-dark: #8a5a1c;
    --green: #58b947;
    --green-soft: #7cc77a;
    --ink: #2b2b2b;
    --tan: #b9a27c;
  }
  * { margin: 0; padding: 0; box-sizing: border-box; }
  html, body { width: 1200px; height: 529px; overflow: hidden; }
  body {
    background: linear-gradient(180deg, #f3f3f3 0%, #d3d3d3 100%);
    font-family: "Comfortaa", sans-serif;
    position: relative;
  }
  .label {
    position: absolute;
    left: 96px; top: 202px;
    width: 997px; height: 201px;
  }
  .label__art { position: absolute; inset: 0; width: 100%; height: 100%; }
  .label__brand {
    position: absolute;
    left: 498px; top: 72px;
    transform: translate(-50%, -50%);
    color: var(--gold);
    font-weight: 700;
    font-size: 15px;
    white-space: nowrap;
  }
  .label__details {
    position: absolute;
    left: 50px; top: 113px;
    color: var(--green);
    font-size: 11.2px;
    line-height: 13px;
  }
  .label__details p + p { margin-top: 4px; }
  .label__title {
    position: absolute;
    left: 0; right: 0; top: 136px;
    text-align: center;
    color: var(--green);
    font-size: 21.5px;
    font-weight: 500;
    letter-spacing: 0.3px;
  }
  .label__weight {
    position: absolute;
    left: 0; right: 0; top: 165px;
    text-align: center;
    color: var(--tan);
    font-size: 10.5px;
  }
  .label__info {
    position: absolute;
    right: 57px; top: 53px;
    text-align: right;
    font-size: 11px;
    line-height: 14.2px;
  }
  .label__info .intro { color: var(--ink); }
  .label__info .steps { color: var(--green); }
  .label__info .storage { color: var(--green); font-size: 9.4px; line-height: 12px; font-weight: 600; }
</style>
</head>
<body>
  <div class="label">
    <svg class="label__art" viewBox="0 0 997 201" aria-hidden="false">
      <defs>
        <linearGradient id="goldLine" x1="0" x2="1">
          <stop offset="0" stop-color="var(--gold-dark)"/>
          <stop offset="0.5" stop-color="var(--gold-light)"/>
          <stop offset="1" stop-color="var(--gold-dark)"/>
        </linearGradient>
        <radialGradient id="leafGlow" cx="0.5" cy="0.6" r="0.6">
          <stop offset="0" stop-color="#5fb55c" stop-opacity="0.8"/>
          <stop offset="1" stop-color="#a9d6a0" stop-opacity="0"/>
        </radialGradient>
      </defs>
      <rect class="band-top" x="0" y="0" width="997" height="48" fill="var(--black)"/>
      <rect class="band-kraft" x="0" y="48" width="997" height="60" fill="var(--kraft)"/>
      <rect class="band-bottom" x="0" y="108" width="997" height="93" fill="var(--black)"/>
      <rect class="rule-gold" x="0" y="42" width="997" height="6" fill="url(#goldLine)"/>
      <g role="img" aria-label="Watercolour green tea leaves">
        <ellipse cx="320" cy="82" rx="120" ry="40" fill="url(#leafGlow)"/>
        <ellipse cx="678" cy="82" rx="120" ry="40" fill="url(#leafGlow)"/>
      </g>
      <path class="swoosh" d="M300,45 C395,45 415,131 498,131 C581,131 601,45 696,45 Z" fill="var(--black)"/>
      <path class="swoosh-edge" d="M300,45 C395,45 415,131 498,131 C581,131 601,45 696,45" fill="none" stroke="url(#goldLine)" stroke-width="3"/>
      <circle class="brand-ring" cx="498" cy="72" r="52" fill="none" stroke="var(--gold)" stroke-width="1.5"/>
      <rect class="badge-nongmo" x="52" y="65" width="52" height="38" rx="3" fill="#2f8fc6"/>
      <circle class="badge-organic" cx="824" cy="163" r="12" fill="#f4f4f4" stroke="#2f7a3a" stroke-width="2"/>
      <line x1="343" y1="168" x2="455" y2="168" stroke="var(--gold)" stroke-width="1"/>
      <line x1="544" y1="168" x2="656" y2="168" stroke="var(--gold)" stroke-width="1"/>
    </svg>

    <div class="label__brand">Lumo Brew</div>

    <div class="label__details">
      <p>Distributed by Lumo Brew Co.|<br>Maple Falls, Ga</p>
      <p>Certified Organic by orvia</p>
      <p>Product of Japan</p>
    </div>

    <h1 class="label__title">Premium Organic Ceremonial Matcha</h1>
    <div class="label__weight">Net Wt: 30 g</div>

    <div class="label__info">
      <div class="intro">Premium Organic Japanese<br>Matcha Green Tea<br>Instructions<br>2 tsp of Matcha</div>
      <div class="steps">2oz of Water (170-180 degrees F)<br>Whisk in a W formation until frothy<br>Sweeten to taste</div>
      <div class="storage">KEEP REFRIGERATED<br>FOR QUALITY</div>
    </div>
  </div>
</body>
</html>
```